General Contractors need a new Crisp updated Card Design

We need a new business card design for our company of 25 years based in Toronto call Holvaster Building Inc. : Our goal is to be the leading commercial contractors in Toronto by providing exceptional value to our clients. We work very hard to deliver professional, quality, service in conjunction with consistent price competitiveness to all of our clients on every single project.

Target Market(s)

Design & Build Clients

Industry/Entity Type

Construction Company

Contact Information for Business Card

Address:
18 North Tamlin Glen Road, Unit 57, Marbrook Vale, ON, K7T 2R9
Office: 905-218-5937

Holvasters Logo
Employee Job Description
Employee Cell Phone #
Employee Email
www.holvaster-example.com

Colors

Designer to choose colors to be used in the design.

Requirements
Must have
• Quote Company Saying:
• "Professional. Quality. Service."
Nice to have
• New Crisp up to date look. simple & fresh ( Not to Busy)
Should not have
• NO BLUE PRINTS ON THE BUSINESS CARDS

```html
<!DOCTYPE html>
<html lang="en">
<head>
<meta charset="utf-8">
<title>Holvaster Building Inc. — Business Card</title>
<link rel="stylesheet" href="https://fonts.googleapis.com/css2?family=Mulish:ital,wght@0,400;0,500;0,800;1,400&display=swap">
<style>
  :root {
    --brand-green: #00695f;
    --card-white: #ffffff;
    --canvas-bg: #eceeed;
    --ink-green: #00695f;
  }
  * { box-sizing: border-box; margin: 0; padding: 0; }
  html, body {
    width: 1200px;
    height: 1200px;
    overflow: hidden;
    background: var(--canvas-bg);
    font-family: "Mulish", sans-serif;
  }
  .canvas {
    width: 1200px;
    height: 1200px;
    display: flex;
    flex-direction: column;
    align-items: center;
    justify-content: center;
    gap: 40px;
  }
  .card {
    width: 840px;
    height: 480px;
    position: relative;
    box-shadow: 0 6px 20px rgba(0,0,0,0.12);
  }
  .card--front {
    background: var(--brand-green);
    color: var(--card-white);
  }
  .card--back {
    background: var(--card-white);
    color: var(--ink-green);
  }
  .brand {
    display: flex;
    align-items: center;
    gap: 18px;
  }
  .brand__mark {
    width: 56px;
    height: 56px;
    flex: none;
  }
  .brand__name {
    font-weight: 800;
    letter-spacing: 0.02em;
    line-height: 1.05;
    text-transform: uppercase;
  }
  .card--front .brand {
    position: absolute;
    left: 200px;
    top: 160px;
  }
  .card--front .brand__mark { width: 84px; height: 84px; }
  .card--front .brand__name { font-size: 40px; }
  .tagline {
    position: absolute;
    left: 200px;
    top: 320px;
    font-size: 26px;
    font-weight: 400;
    letter-spacing: 0.01em;
  }
  .card--back .brand {
    position: absolute;
    left: 60px;
    top: 60px;
  }
  .card--back .brand__name { font-size: 28px; }
  .person {
    position: absolute;
    left: 60px;
    top: 170px;
  }
  .person__name {
    font-size: 28px;
    font-weight: 400;
    letter-spacing: 0.02em;
  }
  .person__name strong { font-weight: 800; }
  .person__role {
    font-size: 19px;
    font-style: italic;
    margin-top: 2px;
  }
  .contact {
    position: absolute;
    right: 60px;
    bottom: 56px;
    text-align: right;
    font-size: 19px;
    line-height: 1.5;
  }
  .contact dt {
    display: inline;
    font-weight: 800;
  }
  .contact dd {
    display: inline;
  }
  .contact dd::after {
    content: "";
    display: block;
  }
</style>
</head>
<body>
<main class="canvas">
  <section class="card card--front" aria-label="Card front">
    <div class="brand">
      <svg class="brand__mark" viewBox="0 0 10 10" aria-hidden="true"><rect width="10" height="10" fill="#ffffff"/></svg>
      <span class="brand__name">Holvaster<br>Building Inc.</span>
    </div>
    <p class="tagline">Professional. Quality. Service.</p>
  </section>

  <section class="card card--back" aria-label="Card back">
    <div class="brand">
      <svg class="brand__mark" viewBox="0 0 10 10" aria-hidden="true"><rect width="10" height="10" fill="#00695f"/></svg>
      <span class="brand__name">Holvaster<br>Building Inc.</span>
    </div>
    <div class="person">
      <p class="person__name">Alden <strong>Rourke</strong></p>
      <p class="person__role">Position</p>
    </div>
    <dl class="contact">
      <dt>Address:</dt> <dd>18 North Tamlin Glen Road,<br>Unit 57, Marbrook Vale, ON, K7T 2R9</dd>
      <dt>Office:</dt> <dd>905-218-5937</dd>
      <dt>Personal:</dt> <dd>905-402-7781</dd>
      <dt>Email:</dt> <dd>arourke@holvaster-example.com</dd>
      <dt>Website:</dt> <dd>www.holvaster-example.com</dd>
    </dl>
  </section>
</main>
</body>
</html>
```